Verpackungen für Schwangerschaftsfotograf
sehr tolle und schnelle Umsetzungen meiner Wünsche - vielen Dank für die gute Zusammenarbeit
Zielgruppe
Fotograf mit Spezialisierung auf Schwangerschaft und Neugeborene
Aufgabenstellung
ich brauche ein Layout für diese Verpackung
https://www.faltwerk-muster.de/download/klappbox/Druckvorlage_FaltwerkMuster_Klappbox-30.pdf
ich stelle mir das vom Design her so vor wie eine Holzkiste:
https://www.bildervorrat-beispiel.com/de/image-photo/wooden-box-483910275?src=QkTzvLwe8pRnYd42h71xkc-1-27
Und wie der Text irgendwie mein Logo integrieren.
Die Schachtel soll eine neue Verpackung werden um Abzüge und USB Stick zu übergeben

```html
<!DOCTYPE html>
<html lang="de">
<head>
<meta charset="utf-8">
<title>Klappbox Holzkiste – Druckvorlage</title>
<link rel="stylesheet" href="https://fonts.googleapis.com/css2?family=Cormorant+Garamond:wght@700&display=swap">
<style>
  :root {
    --paper: #ffffff;
    --wood-base: #9a8470;
    --wood-plank: #b09c86;
    --wood-post: #bba893;
    --wood-dark: #7d6856;
    --wood-seam: #5e4c3e;
    --wood-grain: rgba(90, 70, 55, 0.35);
    --dieline: #e6007e;
    --ink: #111111;
  }
  html, body {
    margin: 0;
    padding: 0;
    width: 799px;
    height: 1200px;
    overflow: hidden;
    background: var(--paper);
  }
  .dieline-sheet { display: block; width: 799px; height: 1200px; }
  .wood-base { fill: var(--wood-base); }
  .plank { fill: var(--wood-plank); }
  .post { fill: var(--wood-post); }
  .board-dark { fill: var(--wood-dark); }
  .seam { stroke: var(--wood-seam); stroke-width: 1.4; fill: none; }
  .grain { stroke: var(--wood-grain); stroke-width: 0.7; fill: none; }
  .plank-edge { fill: none; stroke: var(--wood-seam); stroke-width: 1; }
  .cut-line {
    fill: none;
    stroke: var(--dieline);
    stroke-width: 1.2;
    stroke-linejoin: round;
  }
  .brand-name {
    font-family: "Cormorant Garamond", Georgia, serif;
    font-weight: 700;
    font-size: 10.5px;
    letter-spacing: 0.4px;
    fill: var(--ink);
  }
  .brand-url {
    font-family: "Cormorant Garamond", Georgia, serif;
    font-weight: 700;
    font-size: 9.5px;
    fill: var(--ink);
  }
  .brand-dot { fill: none; stroke: var(--ink); stroke-width: 1.2; }
</style>
</head>
<body>
<svg class="dieline-sheet" viewBox="0 0 799 1200" xmlns="http://www.w3.org/2000/svg">
  <defs>
    <clipPath id="blankShape">
      <rect x="148" y="428" width="460" height="72" rx="10"/>
      <rect x="133" y="495" width="492" height="238" rx="8"/>
      <rect x="69" y="730" width="620" height="62" rx="10"/>
      <rect x="51" y="788" width="650" height="244" rx="8"/>
      <rect x="69" y="1028" width="620" height="61" rx="10"/>
    </clipPath>
  </defs>

  <!-- Holzkisten-Optik: Bretter und Rahmenleisten -->
  <g class="crate-wood" clip-path="url(#blankShape)" role="img" aria-label="Holzkisten-Optik aus verwitterten Brettern mit Rahmenleisten">
    <rect class="wood-base" x="40" y="420" width="680" height="680"/>

    <!-- Einstecklasche -->
    <rect class="board-dark" x="148" y="428" width="43" height="70"/>
    <rect class="board-dark" x="565" y="428" width="43" height="70"/>
    <rect class="post" x="191" y="428" width="41" height="67"/>
    <rect class="post" x="522" y="428" width="39" height="67"/>
    <line class="seam" x1="232" y1="453" x2="522" y2="453"/>
    <line class="grain" x1="232" y1="478" x2="522" y2="478"/>

    <!-- Deckel -->
    <rect class="board-dark" x="133" y="495" width="66" height="238"/>
    <rect class="board-dark" x="557" y="495" width="68" height="238"/>
    <line class="seam" x1="166" y1="495" x2="166" y2="733"/>
    <line class="seam" x1="591" y1="495" x2="591" y2="733"/>
    <rect class="plank" x="199" y="495" width="358" height="35"/>
    <rect class="plank" x="199" y="700" width="358" height="31"/>
    <rect class="post" x="199" y="530" width="33" height="170"/>
    <rect class="post" x="522" y="530" width="35" height="170"/>
    <rect class="plank-edge" x="199" y="495" width="358" height="35"/>
    <rect class="plank-edge" x="199" y="700" width="358" height="31"/>
    <rect class="plank-edge" x="199" y="530" width="33" height="170"/>
    <rect class="plank-edge" x="522" y="530" width="35" height="170"/>
    <line class="seam" x1="232" y1="618" x2="522" y2="618"/>
    <line class="grain" x1="232" y1="575" x2="522" y2="575"/>
    <line class="grain" x1="232" y1="660" x2="522" y2="660"/>

    <!-- Rückwand -->
    <rect class="board-dark" x="69" y="730" width="59" height="58"/>
    <rect class="board-dark" x="630" y="730" width="59" height="58"/>
    <rect class="post" x="191" y="733" width="39" height="57"/>
    <rect class="post" x="520" y="733" width="41" height="57"/>
    <line class="seam" x1="128" y1="733" x2="128" y2="788"/>
    <line class="seam" x1="630" y1="733" x2="630" y2="788"/>
    <line class="grain" x1="230" y1="760" x2="370" y2="760"/>

    <!-- Boden -->
    <rect class="board-dark" x="51" y="788" width="77" height="244"/>
    <rect class="board-dark" x="630" y="788" width="71" height="244"/>
    <line class="seam" x1="160" y1="790" x2="160" y2="1028"/>
    <line class="seam" x1="596" y1="790" x2="596" y2="1028"/>
    <line class="grain" x1="90" y1="790" x2="90" y2="1028"/>
    <line class="grain" x1="666" y1="790" x2="666" y2="1028"/>
    <rect class="plank" x="191" y="790" width="370" height="29"/>
    <rect class="plank" x="191" y="988" width="370" height="40"/>
    <rect class="post" x="199" y="819" width="35" height="169"/>
    <rect class="post" x="523" y="819" width="34" height="169"/>
    <rect class="plank-edge" x="191" y="790" width="370" height="29"/>
    <rect class="plank-edge" x="191" y="988" width="370" height="40"/>
    <rect class="plank-edge" x="199" y="819" width="35" height="169"/>
    <rect class="plank-edge" x="523" y="819" width="34" height="169"/>
    <line class="seam" x1="234" y1="898" x2="523" y2="898"/>
    <line class="grain" x1="234" y1="858" x2="523" y2="858"/>
    <line class="grain" x1="234" y1="945" x2="523" y2="945"/>

    <!-- Bodenlasche -->
    <rect class="board-dark" x="69" y="1028" width="59" height="61"/>
    <rect class="board-dark" x="630" y="1028" width="59" height="61"/>
    <rect class="post" x="191" y="1028" width="39" height="54"/>
    <rect class="post" x="520" y="1028" width="41" height="54"/>
    <line class="seam" x1="128" y1="1030" x2="128" y2="1082"/>
    <line class="seam" x1="630" y1="1030" x2="630" y2="1082"/>
    <line class="grain" x1="230" y1="1058" x2="520" y2="1058"/>
  </g>
  <circle cx="378" cy="428" r="13" fill="var(--paper)"/>

  <!-- Stanzlinien -->
  <g class="dieline">
    <path class="cut-line" d="M158 494 V448 Q158 440 166 440 H190 V437 H355 Q362 437 365 444 Q378 458 391 444 Q394 437 401 437 H565 V440 H590 Q598 440 598 448 V486 Q598 494 590 494 Z"/>
    <line class="cut-line" x1="191" y1="437" x2="191" y2="494"/>
    <line class="cut-line" x1="565" y1="437" x2="565" y2="494"/>
    <rect class="cut-line" x="199" y="495" width="358" height="236"/>
    <path class="cut-line" d="M199 497 L150 502 Q141 503 141 512 V714 Q141 723 150 724 L199 729"/>
    <path class="cut-line" d="M557 497 L606 502 Q615 503 615 512 V714 Q615 723 606 724 L557 729"/>
    <path class="cut-line" d="M78 735 H672 Q678 735 678 742 V770 Q678 784 664 784 H626 L620 790 H130 L124 784 H88 Q77 784 77 772 V742 Q77 735 84 735 Z"/>
    <line class="cut-line" x1="191" y1="735" x2="191" y2="788"/>
    <line class="cut-line" x1="561" y1="735" x2="561" y2="788"/>
    <rect class="cut-line" x="191" y="790" width="370" height="238"/>
    <rect class="cut-line" x="128" y="790" width="63" height="238"/>
    <rect class="cut-line" x="561" y="790" width="69" height="238"/>
    <path class="cut-line" d="M128 794 H70 Q64 794 64 800 V826 Q64 834 70 836 V866 H62 V1000 Q62 1024 80 1024 H128"/>
    <path class="cut-line" d="M630 794 H684 Q690 794 690 800 V826 Q690 834 684 836 V866 H692 V1000 Q692 1024 674 1024 H630"/>
    <rect class="cut-line" x="190" y="832" width="6" height="40" rx="2"/>
    <rect class="cut-line" x="190" y="948" width="6" height="40" rx="2"/>
    <rect class="cut-line" x="556" y="832" width="6" height="40" rx="2"/>
    <rect class="cut-line" x="556" y="948" width="6" height="40" rx="2"/>
    <path class="cut-line" d="M84 1032 H124 L130 1028 H620 L626 1032 H664 Q678 1032 678 1046 V1070 Q678 1082 666 1082 H90 Q77 1082 77 1070 V1044 Q77 1032 84 1032 Z"/>
    <line class="cut-line" x1="191" y1="1030" x2="191" y2="1082"/>
    <line class="cut-line" x1="561" y1="1030" x2="561" y2="1082"/>
  </g>

  <!-- Absender auf der Einstecklasche (kopfstehend) -->
  <g class="brand-lockup" transform="rotate(180 440 474)">
    <circle class="brand-dot" cx="388" cy="471" r="6"/>
    <text class="brand-name" x="400" y="470">JONAS WEBER</text>
    <text class="brand-url" x="400" y="482">babyfoto-musterstadt.de</text>
  </g>

  <!-- Absender auf dem Deckel (kopfstehend) -->
  <g class="brand-lockup" transform="rotate(180 440 549)">
    <circle class="brand-dot" cx="388" cy="546" r="6"/>
    <text class="brand-name" x="400" y="545">JONAS WEBER</text>
    <text class="brand-url" x="400" y="557">babyfoto-musterstadt.de</text>
  </g>

  <!-- Absender auf der Rückwand -->
  <g class="brand-lockup">
    <circle class="brand-dot" cx="378" cy="758" r="6"/>
    <text class="brand-name" x="390" y="757">JONAS WEBER</text>
    <text class="brand-url" x="390" y="769">babyfoto-musterstadt.de</text>
  </g>
</svg>
</body>
</html>
```